New corporate Powerpoint template *

Hi,
We would like to have one new corporate Powerpoint template which can be used for various presentations (Sales, Investors, Marketing, Engineers, HR, Corporate presentations…) Please note that this template will be used for both internal and external presentations.
Please take a look at our website to get a feel for our branding.
https://www.brenvar-microtech.example/

Some visual elements to include:

• The theme needs to be relevant to our industry i.e. Semiconductor theme (circuit board/chip graphic elements)
• Simple uses of color, lifestyle images, moving away from Geometric patterns and colorful wave
• Style should be modern, clean and gender neutral
• Use Korvet blue as more of an accent color - Avoid the overuse of blue (seems a little too bright sometimes)
• Korvet logo to appear on every page

Necessary slides to include:
• Cover Slide
• Agenda Slide
• Divider / Title Slide
• Content Slide
• White Slide
• Comparison slide (two, three, four)
• Table slide with the ability to add rows/columns
• Timeline/roadmap slide
• End Slide

Target Market(s)

Semiconductor industry

Font styles to use
Other font styles liked:
• Arial or Rockwell

Colors
33a6d7

Requirements
Must have
• • The theme needs to be relevant to our industry i.e. Semiconductor theme (circuit board/chip graphic elements)
• • Simple uses of color, lifestyle images
• • Style should be modern, clean and gender neutral
• • Use Korvet blue as more of an accent color
• • Korvet logo to appear on every page
• Necessary slides to include:
• • Cover Slide
• • Agenda Slide
• • Divider / Title Slide
• • Content Slide
• • White Slide
• • Comparison slide (two, three, four)
• • Table slide with the ability to add rows/columns
• • Timeline/roadmap slide
• • End Slide
Nice to have
Should not have
• - Avoid the overuse of blue (seems a little too bright sometimes)
• - Do not use any kind of wave as a graphic

```html
<!DOCTYPE html>
<html lang="en">
<head>
<meta charset="utf-8">
<title>Korvet Corporate Presentation Template</title>
<link href="https://fonts.googleapis.com/css2?family=Open+Sans:wght@400;700&display=swap" rel="stylesheet">
<style>
:root{
  --blue:#2aa3c4;
  --blue-dark:#1b7f99;
  --blue-deep:#176b80;
  --navy:#0f3d4a;
  --grey:#6b6b6b;
  --grey-light:#e9eaeb;
  --ink:#333;
  --canvas:#d8d8d8;
  --white:#fff;
}
*{margin:0;padding:0;box-sizing:border-box}
html,body{width:1200px;height:861px;overflow:hidden;background:var(--canvas);font-family:"Open Sans",Arial,sans-serif;color:var(--ink)}
.slide{position:absolute;width:195px;height:109px;background:var(--white);overflow:hidden;box-shadow:0 0 2px rgba(0,0,0,.15)}
.title{position:absolute;left:6px;top:5px;font-size:3.6px;font-weight:700;letter-spacing:.1px;border-left:1.2px solid var(--blue);padding-left:2.5px;line-height:4px}
.foot{position:absolute;left:6px;bottom:3px;font-size:2.4px;color:#888;display:flex;align-items:center;gap:1.5px}
.foot::before{content:"";width:3px;height:3px;border-radius:50%;background:var(--blue)}
.txt{position:absolute;font-size:2.1px;line-height:2.8px;color:#666}
.txt.w{color:#fff}
.ph{position:absolute;background:linear-gradient(135deg,#3f6a5a,#2b4a42 50%,#7fa29a)}
.ph.chip{background:linear-gradient(135deg,#2e5f4c,#1d3d34 55%,#6a9485)}
.ph.office{background:linear-gradient(135deg,#c7b9a3,#8f8374 50%,#e4ddd2)}
.ph.lab{background:linear-gradient(135deg,#6d9bb3,#2f5368 55%,#b7cdd8)}
.ph.grey{background:linear-gradient(135deg,#d8d8d8,#9a9a9a)}
.band{position:absolute;background:var(--blue)}
.ic{position:absolute;border-radius:50%;background:var(--blue)}
.ic.o{background:transparent;border:.8px solid #fff}
.lbl{position:absolute;font-size:2.6px;font-weight:700;color:var(--blue);text-align:center;line-height:3.2px}
.lbl.w{color:#fff}
.lbl.k{color:#333}
.lbl .role{display:block;font-weight:400;color:#888;font-size:2.2px}
.logo{position:absolute;font-weight:700;color:#fff;display:flex;align-items:center;gap:2px}
.logo::before{content:"";width:5px;height:5px;border-radius:50%;background:currentColor}
.box{position:absolute;border:.6px solid var(--blue);background:#fff}
table{border-collapse:collapse;position:absolute;font-size:2.2px}
td,th{padding:0 1px;height:4.6px}
.product-grid{position:absolute;left:8px;top:22px;width:179px;display:grid;grid-template-columns:repeat(5,1fr);gap:3px 4px}
.product{display:flex;flex-direction:column}
.product .ph{position:static;height:19px;background:linear-gradient(135deg,#f4f4f4,#8d979c)}
.product span{background:var(--blue);color:#fff;font-size:2px;font-weight:700;text-align:center;line-height:3px}
</style>
</head>
<body>

<!-- Row 1 -->
<section class="slide cover" style="left:70px;top:58px;background:linear-gradient(135deg,var(--blue-deep),var(--blue) 60%,var(--blue-dark))">
  <div class="logo" style="left:12px;top:9px;font-size:8px">Korvet</div>
  <div style="position:absolute;right:14px;top:84px;text-align:right;color:#fff;border-right:.8px solid #fff;padding-right:3px">
    <div style="font-size:6px">Corporate Presentation</div>
    <div style="font-size:3px">October 5, 2017</div>
  </div>
</section>

<section class="slide" style="left:287px;top:58px">
  <div class="title">EDIT TITLE HERE</div>
  <div class="band" style="left:6px;top:26px;width:78px;height:66px"></div>
  <p class="txt w" style="left:12px;top:32px;width:46px">Lorem ipsum dolor sit amet, consectetur adipiscing elit, sed do eiusmod tempor incididunt ut labore et dolore magna aliqua ut enim minim.<br><br>Quis nostrud exercitation ullamco laboris nisi ut aliquip ex ea commodo consequat duis aute irure.</p>
  <div class="ph chip" role="img" aria-label="Close-up of a circuit board" style="left:78px;top:26px;width:111px;height:61px"></div>
  <div class="foot">Korvet Microtech</div>
</section>

<section class="slide" style="left:504px;top:58px">
  <div class="title">EDIT TITLE HERE</div>
  <div class="ph grey" role="img" aria-label="Portrait of team member" style="left:24px;top:30px;width:27px;height:27px;border-radius:50%"></div>
  <div class="ph grey" role="img" aria-label="Portrait of team member" style="left:67px;top:30px;width:27px;height:27px;border-radius:50%"></div>
  <div class="ph grey" role="img" aria-label="Portrait of team member" style="left:110px;top:30px;width:27px;height:27px;border-radius:50%"></div>
  <div class="ph grey" role="img" aria-label="Portrait of team member" style="left:153px;top:30px;width:27px;height:27px;border-radius:50%"></div>
  <div class="lbl k" style="left:17px;top:60px;width:41px">MARA LIND<span class="role">General Manager</span></div>
  <div class="lbl k" style="left:60px;top:60px;width:41px">OWEN HALE<span class="role">Product Head</span></div>
  <div class="lbl k" style="left:103px;top:60px;width:41px">THEO MARSH<span class="role">Finance</span></div>
  <div class="lbl k" style="left:146px;top:60px;width:41px">RAVI KOSS<span class="role">Sales Team</span></div>
  <p class="txt" style="left:16px;top:77px;width:165px;text-align:center">Lorem ipsum dolor sit amet, consectetur adipiscing elit, sed do eiusmod tempor incididunt ut labore et dolore magna aliqua. Ut enim ad minim veniam, quis nostrud exercitation ullamco laboris nisi ut aliquip ex ea commodo consequat duis aute irure dolor in reprehenderit.</p>
  <div class="foot">Korvet Microtech</div>
</section>

<section class="slide" style="left:721px;top:58px">
  <div class="title">EDIT TITLE HERE</div>
  <div class="ph lab" role="img" aria-label="Gloved hand holding a chip" style="left:9px;top:20px;width:57px;height:45px"></div>
  <div class="ph chip" role="img" aria-label="Microchips on a board" style="left:70px;top:20px;width:57px;height:45px"></div>
  <div class="ph chip" role="img" aria-label="Processor on a motherboard" style="left:131px;top:20px;width:57px;height:45px"></div>
  <div class="band" style="left:9px;top:64px;width:179px;height:1.2px"></div>
  <div class="lbl" style="left:9px;top:69px;width:57px">LOREM IPSUM</div>
  <div class="lbl" style="left:70px;top:69px;width:57px">LOREM IPSUM</div>
  <div class="lbl" style="left:131px;top:69px;width:57px">LOREM IPSUM</div>
  <p class="txt" style="left:12px;top:74px;width:51px;text-align:center">Lorem ipsum dolor sit amet, consectetur adipiscing elit sed do eiusmod tempor.</p>
  <p class="txt" style="left:73px;top:74px;width:51px;text-align:center">Lorem ipsum dolor sit amet, consectetur adipiscing elit sed do eiusmod tempor.</p>
  <p class="txt" style="left:134px;top:74px;width:51px;text-align:center">Lorem ipsum dolor sit amet, consectetur adipiscing elit sed do eiusmod tempor.</p>
  <div class="foot">Korvet Microtech</div>
</section>

<section class="slide" style="left:936px;top:58px">
  <div class="title">EDIT TITLE HERE</div>
  <div class="ic" style="left:23px;top:27px;width:5px;height:5px"></div>
  <div class="ic" style="left:54px;top:27px;width:5px;height:5px"></div>
  <div class="ic" style="left:85px;top:27px;width:5px;height:5px"></div>
  <div class="ic" style="left:23px;top:65px;width:5px;height:5px"></div>
  <div class="ic" style="left:54px;top:65px;width:5px;height:5px"></div>
  <div class="ic" style="left:85px;top:65px;width:5px;height:5px"></div>
  <p class="txt" style="left:12px;top:35px;width:28px;text-align:center"><b style="color:#333">LOREM IPSUM</b><br>Dolor sit amet, elit sed do eiusmod.</p>
  <p class="txt" style="left:43px;top:35px;width:28px;text-align:center"><b style="color:#333">LOREM IPSUM</b><br>Dolor sit amet, elit sed do eiusmod.</p>
  <p class="txt" style="left:74px;top:35px;width:28px;text-align:center"><b style="color:#333">LOREM IPSUM</b><br>Dolor sit amet, elit sed do eiusmod.</p>
  <p class="txt" style="left:12px;top:73px;width:28px;text-align:center"><b style="color:#333">LOREM IPSUM</b><br>Dolor sit amet, elit sed do eiusmod.</p>
  <p class="txt" style="left:43px;top:73px;width:28px;text-align:center"><b style="color:#333">LOREM IPSUM</b><br>Dolor sit amet, elit sed do eiusmod.</p>
  <p class="txt" style="left:74px;top:73px;width:28px;text-align:center"><b style="color:#333">LOREM IPSUM</b><br>Dolor sit amet, elit sed do eiusmod.</p>
  <div class="ph lab" role="img" aria-label="Wafer inspection under a lab microscope" style="left:112px;top:17px;width:76px;height:60px"></div>
  <div class="foot">Korvet Microtech</div>
</section>

<!-- Row 2 -->
<section class="slide" style="left:70px;top:186px">
  <div class="title">EDIT TITLE HERE</div>
  <div class="ph chip" role="img" aria-label="Technician probing a circuit board" style="left:11px;top:23px;width:71px;height:73px"></div>
  <p class="txt" style="left:92px;top:24px;width:95px">Lorem ipsum dolor sit amet, consectetur adipiscing elit, sed do eiusmod tempor incididunt ut labore et dolore magna aliqua. Ut enim ad minim veniam, quis nostrud exercitation ullamco laboris nisi ut aliquip.</p>
  <div class="ic" style="left:100px;top:66px;width:6px;height:6px;border-radius:1px"></div>
  <div class="ic" style="left:131px;top:66px;width:6px;height:6px;border-radius:1px"></div>
  <div class="ic" style="left:162px;top:66px;width:6px;height:6px;border-radius:1px"></div>
  <p class="txt" style="left:91px;top:76px;width:24px;text-align:center">Lorem ipsum dolor sit amet elit.</p>
  <p class="txt" style="left:122px;top:76px;width:24px;text-align:center">Lorem ipsum dolor sit amet elit.</p>
  <p class="txt" style="left:153px;top:76px;width:24px;text-align:center">Lorem ipsum dolor sit amet elit.</p>
  <div class="foot">Korvet Microtech</div>
</section>

<section class="slide" style="left:287px;top:186px">
  <div class="title">EDIT TITLE HERE</div>
  <p class="txt" style="left:8px;top:20px;width:92px">Lorem ipsum dolor sit amet, consectetur adipiscing elit, sed do eiusmod tempor incididunt ut labore et dolore magna aliqua. Ut enim ad minim veniam, quis nostrud exercitation ullamco laboris nisi ut aliquip ex ea commodo consequat. Duis aute irure dolor in reprehenderit in voluptate velit esse cillum dolore eu fugiat nulla pariatur. Excepteur sint occaecat cupidatat non proident, sunt in culpa qui officia deserunt mollit anim id est laborum. Sed ut perspiciatis unde omnis iste natus error sit voluptatem accusantium.</p>
  <svg style="position:absolute;left:112px;top:30px" width="80" height="60" viewBox="0 0 80 60">
    <g stroke="#ddd" stroke-width=".3"><line x1="6" y1="10" x2="78" y2="10"/><line x1="6" y1="25" x2="78" y2="25"/><line x1="6" y1="40" x2="78" y2="40"/><line x1="6" y1="52" x2="78" y2="52"/></g>
    <g fill="#2aa3c4"><rect x="12" y="42" width="6" height="10"/><rect x="22" y="28" width="6" height="24"/><rect x="32" y="20" width="6" height="32"/><rect x="42" y="12" width="6" height="40"/><rect x="52" y="24" width="6" height="28"/><rect x="62" y="32" width="6" height="20"/></g>
    <rect x="38" y="3" width="14" height="5" fill="#333"/>
  </svg>
  <div class="foot">Korvet Microtech</div>
</section>

<section class="slide" style="left:504px;top:186px">
  <div class="title">EDIT TITLE HERE</div>
  <div class="band" style="left:10px;top:23px;width:53px;height:82px"></div>
  <div class="band" style="left:71px;top:23px;width:53px;height:82px;background:var(--grey)"></div>
  <div class="band" style="left:132px;top:23px;width:53px;height:82px"></div>
  <div class="ic" style="left:28px;top:32px;width:16px;height:13px;background:#fff;border-radius:2px"></div>
  <div class="ic" style="left:89px;top:32px;width:16px;height:13px;background:#fff"></div>
  <div class="ic" style="left:150px;top:32px;width:16px;height:13px;background:#fff;border-radius:1px"></div>
  <p class="txt w" style="left:14px;top:56px;width:45px;text-align:center">Lorem ipsum dolor sit amet, consectetur adipiscing elit, sed do eiusmod tempor incididunt ut labore.</p>
  <p class="txt w" style="left:75px;top:56px;width:45px;text-align:center">Lorem ipsum dolor sit amet, consectetur adipiscing elit, sed do eiusmod tempor incididunt ut labore.</p>
  <p class="txt w" style="left:136px;top:56px;width:45px;text-align:center">Lorem ipsum dolor sit amet, consectetur adipiscing elit, sed do eiusmod tempor incididunt ut labore.</p>
  <div class="foot">Korvet Microtech</div>
</section>

<section class="slide" style="left:721px;top:186px;background:linear-gradient(135deg,var(--blue-deep),var(--blue) 65%)">
  <div class="ic" style="left:22px;top:77px;width:9px;height:8px;background:#fff;border-radius:1px"></div>
  <div style="position:absolute;left:36px;top:74px;color:#fff;border-left:.6px solid #fff;padding-left:3px">
    <div style="font-size:6.5px">Section Title</div>
    <div style="font-size:2.2px">Lorem ipsum dolor sit amet, consectetur adipiscing elit.</div>
  </div>
</section>

<section class="slide" style="left:936px;top:186px">
  <div class="title">EDIT TITLE HERE</div>
  <div style="position:absolute;left:97px;top:22px;width:.5px;height:75px;background:#ccc"></div>
  <div class="ic" style="left:84px;top:28px;width:10px;height:10px"></div>
  <div class="ic" style="left:84px;top:45px;width:10px;height:10px"></div>
  <div class="ic" style="left:84px;top:70px;width:10px;height:10px"></div>
  <div class="ic" style="left:84px;top:87px;width:10px;height:10px"></div>
  <div class="ic" style="left:110px;top:28px;width:10px;height:10px"></div>
  <div class="ic" style="left:110px;top:45px;width:10px;height:10px"></div>
  <div class="ic" style="left:110px;top:70px;width:10px;height:10px"></div>
  <div class="ic" style="left:110px;top:87px;width:10px;height:10px"></div>
  <p class="txt" style="left:20px;top:28px;width:60px;text-align:right"><b style="color:var(--blue)">Lorem ipsum dolor</b><br>Sit amet consectetur elit sed do.</p>
  <p class="txt" style="left:20px;top:45px;width:60px;text-align:right"><b style="color:var(--blue)">Lorem ipsum dolor</b><br>Sit amet consectetur elit sed do.</p>
  <p class="txt" style="left:20px;top:70px;width:60px;text-align:right"><b style="color:var(--blue)">Lorem ipsum dolor</b><br>Sit amet consectetur elit sed do.</p>
  <p class="txt" style="left:20px;top:87px;width:60px;text-align:right"><b style="color:var(--blue)">Lorem ipsum dolor</b><br>Sit amet consectetur elit sed do.</p>
  <p class="txt" style="left:124px;top:28px;width:60px"><b style="color:var(--blue)">Lorem ipsum dolor</b><br>Sit amet consectetur elit sed do.</p>
  <p class="txt" style="left:124px;top:45px;width:60px"><b style="color:var(--blue)">Lorem ipsum dolor</b><br>Sit amet consectetur elit sed do.</p>
  <p class="txt" style="left:124px;top:70px;width:60px"><b style="color:var(--blue)">Lorem ipsum dolor</b><br>Sit amet consectetur elit sed do.</p>
  <p class="txt" style="left:124px;top:87px;width:60px"><b style="color:var(--blue)">Lorem ipsum dolor</b><br>Sit amet consectetur elit sed do.</p>
  <div class="foot">Korvet Microtech</div>
</section>

<!-- Row 3 -->
<section class="slide" style="left:70px;top:316px">
  <div class="title">EDIT TITLE HERE</div>
  <div class="band" style="left:0;top:18px;width:195px;height:80px"></div>
  <p class="txt w" style="left:12px;top:31px;width:38px;font-weight:700;font-size:2.3px;line-height:3px">Lorem ipsum dolor sit amet consectetur adipiscing. Cras bibendum mollis leo, ac efficitur ipsum lobortis nec. Praesent vitae pulvinar orci.</p>
  <div class="box" style="left:56px;top:31px;width:128px;height:48px;border:none"></div>
  <div class="ic" style="left:79px;top:47px;width:7px;height:7px;border-radius:1px"></div>
  <div class="ic" style="left:115px;top:47px;width:7px;height:7px;border-radius:1px"></div>
  <div class="ic" style="left:151px;top:47px;width:7px;height:7px;border-radius:1px"></div>
  <div class="lbl" style="left:67px;top:59px;width:30px">LOREM</div>
  <div class="lbl" style="left:103px;top:59px;width:30px">LOREM</div>
  <div class="lbl" style="left:139px;top:59px;width:30px">LOREM</div>
  <div class="foot">Korvet Microtech</div>
</section>

<section class="slide" style="left:287px;top:316px">
  <div class="title">EDIT TITLE HERE</div>
  <div class="box" style="left:24px;top:26px;width:44px;height:30px"></div>
  <div class="box" style="left:77px;top:26px;width:44px;height:30px"></div>
  <div class="box" style="left:130px;top:26px;width:44px;height:30px"></div>
  <div class="box" style="left:24px;top:67px;width:44px;height:30px"></div>
  <div class="box" style="left:77px;top:67px;width:44px;height:30px"></div>
  <div class="box" style="left:130px;top:67px;width:44px;height:30px"></div>
  <div class="ic" style="left:41px;top:20px;width:10px;height:10px"></div>
  <div class="ic" style="left:94px;top:20px;width:10px;height:10px"></div>
  <div class="ic" style="left:147px;top:20px;width:10px;height:10px"></div>
  <div class="ic" style="left:41px;top:61px;width:10px;height:10px"></div>
  <div class="ic" style="left:94px;top:61px;width:10px;height:10px"></div>
  <div class="ic" style="left:147px;top:61px;width:10px;height:10px"></div>
  <p class="txt" style="left:26px;top:35px;width:40px;text-align:center"><b style="color:#333">Lorem ipsum dolor</b><br>Sit amet consectetur elit sed.</p>
  <p class="txt" style="left:79px;top:35px;width:40px;text-align:center"><b style="color:#333">Lorem ipsum dolor</b><br>Sit amet consectetur elit sed.</p>
  <p class="txt" style="left:132px;top:35px;width:40px;text-align:center"><b style="color:#333">Lorem ipsum dolor</b><br>Sit amet consectetur elit sed.</p>
  <p class="txt" style="left:26px;top:76px;width:40px;text-align:center"><b style="color:#333">Lorem ipsum dolor</b><br>Sit amet consectetur elit sed.</p>
  <p class="txt" style="left:79px;top:76px;width:40px;text-align:center"><b style="color:#333">Lorem ipsum dolor</b><br>Sit amet consectetur elit sed.</p>
  <p class="txt" style="left:132px;top:76px;width:40px;text-align:center"><b style="color:#333">Lorem ipsum dolor</b><br>Sit amet consectetur elit sed.</p>
  <div class="foot">Korvet Microtech</div>
</section>

<section class="slide" style="left:504px;top:316px">
  <div class="title">EDIT TITLE HERE</div>
  <div class="ph chip" role="img" aria-label="Green circuit board with chips" style="left:0;top:22px;width:195px;height:80px"></div>
  <div class="band" style="left:16px;top:22px;width:60px;height:80px;opacity:.85"></div>
  <div class="lbl w" style="left:20px;top:30px;font-size:4px;text-align:left">LOREM IPSUM</div>
  <p class="txt w" style="left:20px;top:37px;width:52px">Lorem ipsum dolor sit amet, consectetur adipiscing elit, sed do eiusmod tempor incididunt ut labore et dolore magna aliqua. Ut enim ad minim veniam, quis nostrud exercitation ullamco laboris nisi ut aliquip ex ea commodo.</p>
  <div class="foot">Korvet Microtech</div>
</section>

<section class="slide" style="left:721px;top:316px">
  <div class="title">EDIT TITLE HERE</div>
  <div class="band" style="left:0;top:22px;width:195px;height:79px"></div>
  <svg style="position:absolute;left:50px;top:30px" width="96" height="42" viewBox="0 0 96 42">
    <g fill="#fff" stroke="#555" stroke-width=".6">
      <rect x="2" y="10" width="22" height="16" rx="1"/><rect x="72" y="10" width="22" height="16" rx="1"/>
      <rect x="28" y="4" width="40" height="28" rx="1"/>
    </g>
    <rect x="20" y="32" width="56" height="2" fill="#ccc"/>
  </svg>
  <div class="logo" style="left:84px;top:41px;font-size:5px;color:var(--blue)">Korvet</div>
  <div class="ic" style="left:58px;top:80px;width:7px;height:7px;background:#fff"></div>
  <div class="ic" style="left:85px;top:80px;width:7px;height:7px;background:#fff"></div>
  <div class="ic" style="left:112px;top:80px;width:7px;height:7px;background:#fff"></div>
  <div class="ic" style="left:139px;top:80px;width:7px;height:7px;background:#fff"></div>
  <div class="foot">Korvet Microtech</div>
</section>

<section class="slide" style="left:936px;top:316px">
  <div class="title">EDIT TITLE HERE</div>
  <table style="left:5px;top:24px;width:185px">
    <tr style="color:#fff;font-weight:700;text-align:center"><th style="background:var(--blue)">Lorem ipsum dolor</th><th style="background:var(--navy)">Lorem ipsum dolor</th><th style="background:var(--blue)">Lorem ipsum dolor</th></tr>
    <tr><td>• Lorem ipsum dolor sit amet</td><td style="background:#f1f1f1">• Lorem ipsum dolor sit amet</td><td style="background:#e6eef7">• Lorem ipsum dolor sit amet</td></tr>
    <tr><td>• Lorem ipsum dolor sit amet</td><td style="background:#f1f1f1">• Lorem ipsum dolor sit amet</td><td style="background:#e6eef7">• Lorem ipsum dolor sit amet</td></tr>
    <tr><td>• Lorem ipsum dolor sit amet</td><td style="background:#f1f1f1">• Lorem ipsum dolor sit amet</td><td style="background:#e6eef7">• Lorem ipsum dolor sit amet</td></tr>
    <tr><td>• Lorem ipsum dolor sit amet</td><td style="background:#f1f1f1">• Lorem ipsum dolor sit amet</td><td style="background:#e6eef7">• Lorem ipsum dolor sit amet</td></tr>
    <tr><td>• Lorem ipsum dolor sit amet</td><td style="background:#f1f1f1">• Lorem ipsum dolor sit amet</td><td style="background:#e6eef7">• Lorem ipsum dolor sit amet</td></tr>
    <tr><td>• Lorem ipsum dolor sit amet</td><td style="background:#f1f1f1">• Lorem ipsum dolor sit amet</td><td style="background:#e6eef7">• Lorem ipsum dolor sit amet</td></tr>
    <tr><td>• Lorem ipsum dolor sit amet</td><td style="background:#f1f1f1">• Lorem ipsum dolor sit amet</td><td style="background:#e6eef7">• Lorem ipsum dolor sit amet</td></tr>
  </table>
  <div class="foot">Korvet Microtech</div>
</section>

<!-- Row 4 -->
<section class="slide" style="left:70px;top:442px">
  <div class="title">EDIT TITLE HERE</div>
  <p class="txt" style="left:9px;top:12px;width:180px;color:#333">Lorem ipsum dolor sit amet, consectetur adipiscing elit. Aenean sed tempor lorem. Suspendisse</p>
  <div class="ph chip" role="img" aria-label="Hands working on a circuit board" style="left:9px;top:18px;width:179px;height:38px"></div>
  <div class="band" style="left:9px;top:65px;width:40px;height:6px;background:var(--navy)"></div>
  <div class="band" style="left:55px;top:65px;width:40px;height:6px"></div>
  <div class="band" style="left:101px;top:65px;width:40px;height:6px;background:var(--navy)"></div>
  <div class="band" style="left:147px;top:65px;width:40px;height:6px"></div>
  <div class="lbl w" style="left:9px;top:66.5px;width:40px">A</div>
  <div class="lbl w" style="left:55px;top:66.5px;width:40px">B</div>
  <div class="lbl w" style="left:101px;top:66.5px;width:40px">C</div>
  <div class="lbl w" style="left:147px;top:66.5px;width:40px">D</div>
  <p class="txt" style="left:10px;top:75px;width:38px;text-align:center">Lorem ipsum dolor sit amet, elit sed do eiusmod tempor.</p>
  <p class="txt" style="left:56px;top:75px;width:38px;text-align:center">Lorem ipsum dolor sit amet, elit sed do eiusmod tempor.</p>
  <p class="txt" style="left:102px;top:75px;width:38px;text-align:center">Lorem ipsum dolor sit amet, elit sed do eiusmod tempor.</p>
  <p class="txt" style="left:148px;top:75px;width:38px;text-align:center">Lorem ipsum dolor sit amet, elit sed do eiusmod tempor.</p>
  <div class="foot">Korvet Microtech</div>
</section>

<section class="slide" style="left:287px;top:442px">
  <div class="title">EDIT TITLE HERE</div>
  <table style="left:14px;top:33px;width:168px;text-align:center">
    <tr style="background:var(--blue);color:#fff;font-weight:700"><th>Lorem</th><th>Lorem</th><th>Lorem</th><th>Lorem</th></tr>
    <tr style="background:#e9eaeb"><td>Lorem</td><td>Lorem</td><td>Lorem</td><td>Lorem</td></tr>
    <tr style="background:#fff"><td>Lorem</td><td>Lorem</td><td>Lorem</td><td>Lorem</td></tr>
    <tr style="background:#e9eaeb"><td>Lorem</td><td>Lorem</td><td>Lorem</td><td>Lorem</td></tr>
    <tr style="background:#fff"><td>Lorem</td><td>Lorem</td><td>Lorem</td><td>Lorem</td></tr>
    <tr style="background:#e9eaeb"><td>Lorem</td><td>Lorem</td><td>Lorem</td><td>Lorem</td></tr>
    <tr style="background:#fff"><td>Lorem</td><td>Lorem</td><td>Lorem</td><td>Lorem</td></tr>
  </table>
  <div class="foot">Korvet Microtech</div>
</section>

<section class="slide" style="left:504px;top:442px">
  <div class="title">EDIT TITLE HERE</div>
  <p class="txt" style="left:9px;top:12px;width:180px">Lorem ipsum dolor sit amet, consectetur adipiscing elit, sed do eiusmod tempor incididunt ut labore et dolore magna aliqua.</p>
  <div class="band" style="left:0;top:29px;width:195px;height:65px"></div>
  <svg style="position:absolute;left:8px;top:36px" width="50" height="46" viewBox="0 0 50 46">
    <rect x="2" y="2" width="46" height="32" fill="#fff" stroke="#444" stroke-width="1.2"/>
    <rect x="20" y="34" width="10" height="7" fill="#ccc"/><rect x="14" y="41" width="22" height="2" fill="#bbb"/>
  </svg>
  <div class="ic o" style="left:79px;top:53px;width:9px;height:9px"></div>
  <div class="ic o" style="left:112px;top:53px;width:9px;height:9px"></div>
  <div class="ic o" style="left:145px;top:53px;width:9px;height:9px"></div>
  <div class="ic o" style="left:176px;top:53px;width:9px;height:9px"></div>
  <p class="txt w" style="left:72px;top:66px;width:23px;text-align:center">Lorem ipsum dolor sit.</p>
  <p class="txt w" style="left:105px;top:66px;width:23px;text-align:center">Lorem ipsum dolor sit.</p>
  <p class="txt w" style="left:138px;top:66px;width:23px;text-align:center">Lorem ipsum dolor sit.</p>
  <p class="txt w" style="left:169px;top:66px;width:23px;text-align:center">Lorem ipsum dolor sit.</p>
  <div class="foot">Korvet Microtech</div>
</section>

<section class="slide" style="left:721px;top:442px">
  <div class="ph" role="img" aria-label="Laptop showing business charts" style="inset:0;background:linear-gradient(135deg,#c9d4dc,#6e8596 55%,#dde5ea)"></div>
  <div class="band" style="left:30px;top:0;width:60px;height:109px;background:rgba(30,60,75,.78)"></div>
  <div style="position:absolute;left:38px;top:32px;color:#fff">
    <div style="font-size:6px">Section Title</div>
    <p style="font-size:2.3px;line-height:3px;width:44px;margin-top:2px">Lorem ipsum dolor sit amet, consectetur adipiscing elit, sed do eiusmod tempor incididunt ut labore et dolore magna.</p>
  </div>
</section>

<section class="slide" style="left:936px;top:442px">
  <div class="title">EDIT TITLE HERE</div>
  <svg style="position:absolute;left:8px;top:26px" width="132" height="70" viewBox="0 0 132 70">
    <g stroke="#ddd" stroke-width=".3"><line x1="6" y1="10" x2="130" y2="10"/><line x1="6" y1="25" x2="130" y2="25"/><line x1="6" y1="40" x2="130" y2="40"/><line x1="6" y1="55" x2="130" y2="55"/></g>
    <polygon points="6,55 6,30 40,22 75,34 100,16 130,30 130,55" fill="#c7dff0"/>
    <polygon points="6,55 6,40 40,32 75,40 100,24 130,38 130,55" fill="#2aa3c4"/>
    <polygon points="6,55 6,46 40,42 75,46 100,34 130,46 130,55" fill="#1b7f99"/>
    <polygon points="6,55 6,50 40,50 75,52 100,44 130,52 130,55" fill="#0f3d4a"/>
    <g fill="#2aa3c4"><rect x="32" y="14" width="12" height="4"/><rect x="92" y="8" width="12" height="4"/><rect x="112" y="22" width="12" height="4"/></g>
    <g fill="#888" font-size="2.4"><text x="10" y="65">Lorem</text><text x="40" y="65">Lorem</text><text x="70" y="65">Lorem</text><text x="100" y="65">Lorem</text></g>
  </svg>
  <p class="txt" style="left:143px;top:24px;width:46px;text-align:right">Lorem ipsum dolor sit amet, consectetur adipiscing elit, sed do eiusmod tempor incididunt ut labore et dolore magna aliqua. Ut enim ad minim veniam, quis nostrud exercitation ullamco laboris nisi ut aliquip ex ea commodo consequat duis aute irure dolor in reprehenderit voluptate.</p>
  <div class="foot">Korvet Microtech</div>
</section>

<!-- Row 5 -->
<section class="slide" style="left:70px;top:569px">
  <div class="title">EDIT TITLE HERE</div>
  <svg style="position:absolute;left:10px;top:22px" width="175" height="62" viewBox="0 0 175 62">
    <g fill="none" stroke-width="9">
      <path d="M50 58 A40 40 0 0 1 62 30" stroke="#2aa3c4"/>
      <path d="M64 28 A40 40 0 0 1 86 18" stroke="#1b7f99"/>
      <path d="M90 18 A40 40 0 0 1 112 28" stroke="#2aa3c4"/>
      <path d="M114 30 A40 40 0 0 1 126 58" stroke="#1b7f99"/>
    </g>
    <g fill="#5a5a5a"><rect x="30" y="4" width="32" height="8"/><rect x="120" y="4" width="28" height="8"/><rect x="146" y="28" width="28" height="8"/></g>
    <rect x="4" y="28" width="28" height="8" fill="#2aa3c4"/>
    <g fill="#fff" font-size="2.4" font-weight="700"><text x="34" y="9">EDIT TITLE HERE</text><text x="123" y="9">EDIT TITLE HERE</text><text x="149" y="33">EDIT TITLE</text><text x="7" y="33">EDIT TITLE</text></g>
    <circle cx="88" cy="44" r="3" fill="#666"/><rect x="86" y="47" width="4" height="10" fill="#666"/>
  </svg>
  <p class="txt" style="left:10px;top:88px;width:176px">Lorem ipsum dolor sit amet, consectetur adipiscing elit, sed do eiusmod tempor incididunt ut labore et dolore magna aliqua ut enim ad minim veniam quis nostrud.</p>
  <div class="foot">Korvet Microtech</div>
</section>

<section class="slide" style="left:287px;top:569px;background:var(--grey-light)">
  <div class="title" style="background:#fff;left:0;top:0;width:195px;padding:5px 6px 4px 9px;border-left:none">EDIT TITLE HERE</div>
  <div class="product-grid">
    <div class="product"><div class="ph" role="img" aria-label="Product photo"></div><span>LOREM</span></div>
    <div class="product"><div class="ph" role="img" aria-label="Product photo"></div><span>LOREM</span></div>
    <div class="product"><div class="ph" role="img" aria-label="Product photo"></div><span>LOREM</span></div>
    <div class="product"><div class="ph" role="img" aria-label="Product photo"></div><span>LOREM</span></div>
    <div class="product"><div class="ph" role="img" aria-label="Product photo"></div><span>LOREM</span></div>
    <div class="product"><div class="ph" role="img" aria-label="Product photo"></div><span>LOREM</span></div>
    <div class="product"><div class="ph" role="img" aria-label="Product photo"></div><span>LOREM</span></div>
    <div class="product"><div class="ph" role="img" aria-label="Product photo"></div><span>LOREM</span></div>
    <div class="product"><div class="ph" role="img" aria-label="Product photo"></div><span>LOREM</span></div>
    <div class="product"><div class="ph" role="img" aria-label="Product photo"></div><span>LOREM</span></div>
    <div class="product"><div class="ph" role="img" aria-label="Product photo"></div><span>LOREM</span></div>
    <div class="product"><div class="ph" role="img" aria-label="Product photo"></div><span>LOREM</span></div>
    <div class="product"><div class="ph" role="img" aria-label="Product photo"></div><span>LOREM</span></div>
    <div class="product"><div class="ph" role="img" aria-label="Product photo"></div><span>LOREM</span></div>
    <div class="product"><div class="ph" role="img" aria-label="Product photo"></div><span>LOREM</span></div>
  </div>
  <div class="foot">Korvet Microtech</div>
</section>

<section class="slide" style="left:504px;top:569px">
  <div class="title">EDIT TITLE HERE</div>
  <svg style="position:absolute;left:20px;top:18px" width="160" height="62" viewBox="0 0 160 62">
    <g stroke="#2aa3c4" stroke-width=".5" fill="none">
      <path d="M80 9 V14 M20 14 H140 M20 14 V18 M60 14 V18 M100 14 V18 M140 14 V18 M60 23 V48 M100 23 V48 M60 31 H64 M60 45 H64 M100 31 H96"/>
    </g>
    <rect x="66" y="3" width="28" height="6" fill="#2aa3c4"/>
    <g fill="#0f3d4a"><rect x="6" y="18" width="28" height="6"/><rect x="126" y="18" width="28" height="6"/></g>
    <g fill="#2aa3c4"><rect x="46" y="18" width="28" height="6"/><rect x="86" y="18" width="28" height="6"/><rect x="66" y="29" width="28" height="6"/><rect x="46" y="40" width="28" height="6"/><rect x="86" y="40" width="28" height="6"/><rect x="66" y="51" width="28" height="6"/></g>
    <g fill="#fff" font-size="2.3" font-weight="700" text-anchor="middle"><text x="80" y="6.8">Title Goes Here</text><text x="20" y="21.8">Title Goes Here</text><text x="60" y="21.8">Title Goes Here</text><text x="100" y="21.8">Title Goes Here</text><text x="140" y="21.8">Title Goes Here</text><text x="80" y="32.8">Title Goes Here</text><text x="60" y="43.8">Title Goes Here</text><text x="100" y="43.8">Title Goes Here</text><text x="80" y="54.8">Title Goes Here</text></g>
  </svg>
  <p class="txt" style="left:10px;top:88px;width:176px">Lorem ipsum dolor sit amet, consectetur adipiscing elit, sed do eiusmod tempor incididunt ut labore et dolore magna aliqua ut enim ad minim veniam quis nostrud.</p>
  <div class="foot">Korvet Microtech</div>
</section>

<section class="slide" style="left:721px;top:569px">
  <div class="title">EDIT TITLE HERE</div>
  <div class="band" style="left:0;top:22px;width:195px;height:48px;background:var(--grey-light)"></div>
  <div class="band" style="left:32px;top:42px;width:44px;height:22px"></div>
  <div class="band" style="left:82px;top:42px;width:44px;height:22px;background:#5a5a5a"></div>
  <div class="band" style="left:132px;top:42px;width:44px;height:22px"></div>
  <div class="ic" style="left:35px;top:37px;width:9px;height:9px;border:.8px solid #fff"></div>
  <div class="ic" style="left:85px;top:37px;width:9px;height:9px;background:#5a5a5a;border:.8px solid #fff"></div>
  <div class="ic" style="left:135px;top:37px;width:9px;height:9px;border:.8px solid #fff"></div>
  <p class="txt w" style="left:46px;top:47px;width:28px"><b>Lorem ipsum</b><br>Dolor sit amet elit sed do.</p>
  <p class="txt w" style="left:96px;top:47px;width:28px"><b>Lorem ipsum</b><br>Dolor sit amet elit sed do.</p>
  <p class="txt w" style="left:146px;top:47px;width:28px"><b>Lorem ipsum</b><br>Dolor sit amet elit sed do.</p>
  <p class="txt" style="left:32px;top:77px;width:144px">Lorem ipsum dolor sit amet, consectetur adipiscing elit, sed do eiusmod tempor incididunt ut labore et dolore magna aliqua ut enim ad minim veniam.</p>
  <div class="foot">Korvet Microtech</div>
</section>

<section class="slide" style="left:936px;top:569px">
  <div class="title">EDIT TITLE HERE</div>
  <div class="band" style="left:0;top:22px;width:195px;height:63px"></div>
  <svg style="position:absolute;left:44px;top:36px" width="60" height="40" viewBox="0 0 60 40">
    <rect x="8" y="2" width="44" height="30" rx="1.5" fill="#fff" stroke="#444" stroke-width="1"/>
    <rect x="2" y="32" width="56" height="3" rx="1" fill="#ccc"/>
  </svg>
  <div class="logo" style="left:60px;top:46px;font-size:5.5px;color:var(--blue)">Korvet</div>
  <svg style="position:absolute;left:118px;top:38px" width="8" height="40" viewBox="0 0 8 40">
    <g fill="#fff"><circle cx="4" cy="4" r="3"/><circle cx="4" cy="18" r="3"/><circle cx="4" cy="32" r="3"/></g>
    <g stroke="#2aa3c4" stroke-width=".8" fill="none"><path d="M2.5 4 L3.7 5.2 L5.6 2.9"/><path d="M2.5 18 L3.7 19.2 L5.6 16.9"/><path d="M2.5 32 L3.7 33.2 L5.6 30.9"/></g>
  </svg>
  <p class="txt w" style="left:129px;top:38px;width:55px"><b>Lorem ipsum</b><br>Dolor sit amet consectetur elit.</p>
  <p class="txt w" style="left:129px;top:52px;width:55px"><b>Lorem ipsum</b><br>Dolor sit amet consectetur elit.</p>
  <p class="txt w" style="left:129px;top:66px;width:55px"><b>Lorem ipsum</b><br>Dolor sit amet consectetur elit.</p>
  <p class="txt" style="left:10px;top:89px;width:176px">Lorem ipsum dolor sit amet, consectetur adipiscing elit, sed do eiusmod tempor incididunt ut labore et dolore magna aliqua ut enim ad minim veniam quis nostrud.</p>
  <div class="foot">Korvet Microtech</div>
</section>

<!-- Row 6 -->
<section class="slide" style="left:287px;top:698px;background:var(--grey-light)">
  <div class="title" style="background:#fff;left:0;top:0;width:195px;padding:5px 6px 4px 9px;border-left:none">EDIT TITLE HERE</div>
  <div class="ph office" role="img" aria-label="Team meeting" style="left:17px;top:25px;width:50px;height:25px"></div>
  <div class="ph office" role="img" aria-label="Team meeting" style="left:73px;top:25px;width:50px;height:25px"></div>
  <div class="ph office" role="img" aria-label="Team meeting" style="left:129px;top:25px;width:50px;height:25px"></div>
  <div class="ph office" role="img" aria-label="Team meeting" style="left:17px;top:63px;width:50px;height:25px"></div>
  <div class="ph office" role="img" aria-label="Team meeting" style="left:73px;top:63px;width:50px;height:25px"></div>
  <div class="ph office" role="img" aria-label="Team meeting" style="left:129px;top:63px;width:50px;height:25px"></div>
  <div class="band" style="left:17px;top:51px;width:50px;height:5px"></div>
  <div class="band" style="left:73px;top:51px;width:50px;height:5px"></div>
  <div class="band" style="left:129px;top:51px;width:50px;height:5px"></div>
  <div class="band" style="left:17px;top:89px;width:50px;height:5px"></div>
  <div class="band" style="left:73px;top:89px;width:50px;height:5px"></div>
  <div class="band" style="left:129px;top:89px;width:50px;height:5px"></div>
  <div class="lbl w" style="left:17px;top:52px;width:50px;font-size:2.2px">LOREM IPSUM DOLOR</div>
  <div class="lbl w" style="left:73px;top:52px;width:50px;font-size:2.2px">LOREM IPSUM DOLOR</div>
  <div class="lbl w" style="left:129px;top:52px;width:50px;font-size:2.2px">LOREM IPSUM DOLOR</div>
  <div class="lbl w" style="left:17px;top:90px;width:50px;font-size:2.2px">LOREM IPSUM DOLOR</div>
  <div class="lbl w" style="left:73px;top:90px;width:50px;font-size:2.2px">LOREM IPSUM DOLOR</div>
  <div class="lbl w" style="left:129px;top:90px;width:50px;font-size:2.2px">LOREM IPSUM DOLOR</div>
  <div class="foot">Korvet Microtech</div>
</section>

<section class="slide" style="left:504px;top:698px">
  <div class="title">EDIT TITLE HERE</div>
  <div class="ph" role="img" aria-label="World map with office location markers" style="left:20px;top:20px;width:160px;height:62px;background:linear-gradient(180deg,#e4e4e4,#cfcfcf)"></div>
  <div class="ic" style="left:12px;top:86px;width:4px;height:4px;background:var(--navy)"></div>
  <div class="ic" style="left:12px;top:95px;width:4px;height:4px"></div>
  <div class="lbl k" style="left:19px;top:86px;font-size:2.2px;line-height:4px">EDIT TITLE HERE</div>
  <div class="lbl k" style="left:19px;top:95px;font-size:2.2px;line-height:4px">EDIT TITLE HERE</div>
  <div class="foot">Korvet Microtech</div>
</section>

<section class="slide" style="left:721px;top:698px">
  <div class="ph office" role="img" aria-label="Cheerful business team in an office" style="inset:0;background:linear-gradient(135deg,#6b6660,#c9a98a 55%,#f2e6d6)"></div>
  <div class="band" style="left:25px;top:0;width:54px;height:109px;opacity:.85"></div>
  <div style="position:absolute;left:25px;top:50px;width:54px;text-align:center;color:#fff;font-size:6.5px;font-weight:700">THANK YOU</div>
</section>

</body>
</html>
```